Business Card: RW Office Partners - Your tidy answer finder

Business Name: RW Office Partners
Website: www.rwofficepartners.com.au
Email: marisol@rwofficepartners.com.au
Mobile: 61 487 902 346
Facebook: @rwofficepartners
Instrgram: @rwofficepartners

Brading Colours:
HEX
#986474
#ddccd3
#7a8498
#c9d8e4
#000000
#ffffff

Tag Line: Your organised problem solver

Link to DRAFT website:
https://helpdeskhub.sitebuilderx.com/rw-office-partners

About Page from the website:
My name is Marisol Bramwell, and I would love to assist you to become more productive in your day to day and achieve your business and personal goals.
My mission is to give you time, time to work on the important tasks of your business or to be able to spend more time with your family. I will take on the tasks you don’t have time for, don’t know well or simply don’t like to do.
I have an extensive background in Administration, Tender Coordination, Document Control, WHS and Quality Management working primarily in the Construction, Mining and Corporate World.
I am passionate about being organised, having order and making things in your life (and mine) easier! I love to watch something unfold and grow into something amazing! I am known for being the go-to problem solver, the organiser of all things, producing high standards of work even under pressure. I’m also a confident communicator, and I understand that you’re busy running your business.

Target Market(s)

Small to Medium Business who require assistance in their business by a virtual assistant.

Industry/Entity Type

Virtual Assistant

Contact Information for Business Card

Mobile: 61 487 902 346

Font styles to use
Sans Serif

Colors
ffffff

Requirements
Must have
• Branding Colours as outlined.
Contact Details as outlined.
Logo as provided.
Proper contact details - mobile, facebook, instragm, website.
Simple, Elegant, very clean looking.
Should not have
• Note cute with pictures.
Not too girly as still want to market to construction companies.

```html
<!DOCTYPE html>
<html lang="en">
<head>
<meta charset="utf-8">
<title>RW Office Partners – Business Card</title>
<link href="https://fonts.googleapis.com/css2?family=Montserrat:wght@500;700&family=Arimo:wght@400&display=swap" rel="stylesheet">
<style>
  :root {
    --mauve: #986474;
    --navy: #232833;
    --slate: #7a8498;
    --grey-text: #6b6b6f;
    --rule: #6f6f73;
    --paper: #ffffff;
    --backdrop: #bdbbbc;
  }
  * { margin: 0; padding: 0; box-sizing: border-box; }
  html, body { width: 1200px; height: 943px; overflow: hidden; }
  body {
    background: var(--backdrop);
    font-family: "Arimo", Arial, sans-serif;
    position: relative;
  }
  .card {
    position: absolute;
    left: 240px;
    width: 720px;
    height: 411px;
    box-shadow: 0 10px 24px rgba(0,0,0,0.25);
  }
  .card-front { top: 40px; background: var(--navy); }
  .card-back { top: 492px; background: var(--paper); }

  .brand {
    position: absolute;
    display: flex;
    align-items: center;
    gap: 14px;
    font-family: "Montserrat", sans-serif;
    font-weight: 500;
    text-transform: uppercase;
    letter-spacing: 1.5px;
    line-height: 1.05;
  }
  .brand-mark { width: 34px; height: 34px; background: var(--mauve); flex: none; }
  .card-front .brand { left: 50%; top: 50%; transform: translate(-50%, -50%); font-size: 36px; color: var(--paper); }
  .card-front .brand-mark { width: 44px; height: 44px; }
  .card-back .brand { left: 70px; top: 218px; font-size: 25px; color: var(--slate); }

  .divider {
    position: absolute;
    left: 372px;
    top: 96px;
    width: 1.5px;
    height: 196px;
    background: var(--rule);
  }
  .contact {
    position: absolute;
    left: 394px;
    top: 92px;
  }
  .person-name {
    font-family: "Montserrat", sans-serif;
    font-weight: 700;
    font-size: 23px;
    color: var(--mauve);
  }
  .person-title { font-size: 13px; color: var(--grey-text); margin: 2px 0 16px 10px; }
  .contact-list { list-style: none; }
  .contact-list li {
    display: flex;
    align-items: center;
    gap: 10px;
    font-size: 13.5px;
    color: var(--grey-text);
    height: 22px;
    margin-left: 10px;
  }
  .contact-list svg { width: 16px; height: 16px; flex: none; }
  .tagline {
    position: absolute;
    left: 394px;
    top: 350px;
    font-size: 17px;
    color: var(--grey-text);
    letter-spacing: 0.3px;
  }
</style>
</head>
<body>
  <section class="card card-front">
    <div class="brand"><span class="brand-mark"></span><span>RW Office<br>Partners</span></div>
  </section>

  <section class="card card-back">
    <div class="brand"><span class="brand-mark"></span><span>RW Office<br>Partners</span></div>
    <div class="divider"></div>
    <div class="contact">
      <p class="person-name">Marisol Bramwell</p>
      <p class="person-title">Title</p>
      <ul class="contact-list">
        <li>
          <svg viewBox="0 0 16 16"><rect x="4" y="1" width="8" height="14" rx="1.5" fill="none" stroke="#986474" stroke-width="1.3"/><circle cx="8" cy="12.5" r="0.8" fill="#986474"/></svg>
          61 487 902 346
        </li>
        <li>
          <svg viewBox="0 0 16 16"><rect x="1" y="3.5" width="14" height="9" fill="#986474"/><path d="M1 3.5 L8 9 L15 3.5" fill="none" stroke="#fff" stroke-width="1"/></svg>
          marisol@rwofficepartners.com.au
        </li>
        <li>
          <svg viewBox="0 0 16 16" fill="none" stroke="#986474" stroke-width="1"><circle cx="8" cy="8" r="6.5"/><ellipse cx="8" cy="8" rx="3" ry="6.5"/><path d="M1.5 8h13M2.5 5h11M2.5 11h11"/></svg>
          www.rwofficepartners.com.au
        </li>
        <li>
          <svg viewBox="0 0 16 16"><circle cx="8" cy="8" r="6" fill="#986474"/></svg>
          @rwofficepartners
        </li>
        <li>
          <svg viewBox="0 0 16 16"><circle cx="8" cy="8" r="6" fill="#986474"/></svg>
          @rwofficepartners
        </li>
      </ul>
    </div>
    <p class="tagline">Your tidy answer finder</p>
  </section>
</body>
</html>
```